TITLE: What Makes My Child’s Playing Talent Grow? SUB-TITLE: A Mother’s Plain Talk Manual for Coaching...

My book is for parents who have young children that are really into sports. My book empowers parents so they can motivate their children to succeed. It deals with sports psychology. Both my title and subtitle should be easy to read. Ideally, I would like a picture of young athlete(s) on the title. I have uploaded files of some books on Brindlemart that deal with the same subject. The last two files are 1) my company logo, please try to include these colors 2) an ebook cover I put together myself. You will notice an On-line bonus in the middle of the book, this Bonus needs to be on the cover.

Target Market(s)

Parents with children who play sports at a high level

Colors

Designer to choose colors to be used in the design.

Requirements
Must have
• Online Bonus feature as per my example.
• Dimensions: Pagelux = The ideal size of your eBook cover art is a height/width ratio of 1.6:1. This means that for every 1,000 pixels in width, the image should be 1,600 pixels in height.
Nice to have
• picture of a young athlete or young athletes

```html
<!DOCTYPE html>
<html lang="en">
<head>
<meta charset="utf-8">
<title>What Makes My Child’s Playing Talent Grow? – Book Cover</title>
<link href="https://fonts.googleapis.com/css2?family=Montserrat:ital,wght@0,400;0,600;0,700;0,800;1,800;1,900&display=swap" rel="stylesheet">
<style>
  :root {
    --page: #ffffff;
    --cover: #111213;
    --title-box: #262b2e;
    --accent: #f7a325;
    --text-light: #ffffff;
    --text-dark: #151515;
  }
  html, body {
    margin: 0;
    padding: 0;
    width: 1200px;
    height: 1200px;
    overflow: hidden;
    background: var(--page);
  }
  .canvas {
    position: relative;
    width: 1200px;
    height: 1200px;
    font-family: "Montserrat", Arial, sans-serif;
  }
  .cover {
    position: absolute;
    left: 246px;
    top: 34px;
    width: 708px;
    height: 1132px;
    background: var(--cover);
    overflow: hidden;
  }
  .photo-strip {
    position: absolute;
    left: 0;
    top: 0;
    width: 708px;
    height: 435px;
    display: flex;
  }
  .photo {
    height: 100%;
  }
  .photo--badminton { width: 176px; background: radial-gradient(ellipse at 45% 55%, #1b5fa8 0%, #0b2340 40%, #000 75%); }
  .photo--hockey { width: 178px; background: linear-gradient(180deg, #1c3452 0%, #2c5580 45%, #b9cfe0 85%, #dfe9f1 100%); }
  .photo--football { width: 178px; background: linear-gradient(180deg, #0f2430 0%, #3a5a5c 35%, #c4402c 55%, #2f5a26 85%, #3e7a2c 100%); }
  .photo--gymnast { width: 176px; background: linear-gradient(180deg, #eeeeee 0%, #e2e2e4 60%, #d8d8dc 100%); }

  .bonus-badge {
    position: absolute;
    left: 346px;
    top: 390px;
    width: 252px;
    height: 186px;
  }

  .title-stack {
    position: absolute;
    left: 110px;
    top: 612px;
    width: 488px;
  }
  .title-line {
    height: 76px;
    margin-bottom: 12px;
    background: var(--title-box);
    display: flex;
    align-items: center;
    justify-content: center;
    font-style: italic;
    white-space: nowrap;
  }
  .title-line--lead { font-weight: 800; font-size: 34px; color: var(--text-light); }
  .title-line--accent { font-weight: 900; font-size: 46px; color: var(--accent); text-transform: uppercase; letter-spacing: -1px; }
  .title-line--close { font-weight: 900; font-size: 54px; color: var(--text-light); text-transform: uppercase; }

  .subtitle {
    position: absolute;
    left: 0;
    top: 892px;
    width: 708px;
    text-align: center;
    color: var(--text-light);
    font-size: 21px;
    line-height: 27px;
    font-weight: 400;
    margin: 0;
  }

  .footer-band {
    position: absolute;
    left: 0;
    top: 990px;
    width: 708px;
    height: 142px;
    background: linear-gradient(180deg, #2c2c2c 0%, #151515 40%, #000 100%);
  }
  .brand {
    position: absolute;
    left: 0;
    top: 30px;
    width: 708px;
    display: flex;
    justify-content: center;
    align-items: center;
    gap: 10px;
  }
  .brand-dot {
    width: 22px;
    height: 22px;
    border-radius: 50%;
    background: var(--accent);
  }
  .brand-name {
    color: var(--accent);
    font-size: 18px;
    font-weight: 600;
    letter-spacing: 1px;
    text-transform: uppercase;
  }
  .author {
    position: absolute;
    left: 0;
    top: 90px;
    width: 708px;
    text-align: center;
    color: var(--text-light);
    font-size: 25px;
    font-weight: 700;
    letter-spacing: 0.5px;
  }
</style>
</head>
<body>
<div class="canvas">
  <div class="cover">
    <div class="photo-strip">
      <div class="photo photo--badminton" role="img" aria-label="Young badminton player leaping with light trails on a dark background"></div>
      <div class="photo photo--hockey" role="img" aria-label="Young ice hockey player in helmet skating with a stick"></div>
      <div class="photo photo--football" role="img" aria-label="Young footballer in red kit kicking a ball in a stadium"></div>
      <div class="photo photo--gymnast" role="img" aria-label="Young rhythmic gymnast holding a high leg with a ribbon"></div>
    </div>

    <svg class="bonus-badge" viewBox="0 0 252 186" aria-label="Free online workshop bonus, $170 value">
      <polygon fill="var(--accent)" points="
        126,6 133,20 144,8 148,23 161,13 162,28 176,21 174,36 189,32 184,46 199,45 191,58 205,60 195,71 208,76 196,84 207,91 194,97 203,106 190,110 197,120 183,122 188,133 174,133 176,145 162,142 162,155 149,149 146,162 134,154 129,166 120,155 113,166 106,153 97,162 93,148 81,155 79,141 66,144 67,130 53,131 57,118 44,116 51,105 38,100 48,91 36,85 48,77 38,69 51,63 43,53 57,51 53,39 67,40 66,27 79,31 81,18 93,25 98,12 108,21 115,8 120,20" />
      <circle cx="126" cy="86" r="62" fill="#ffffff"/>
      <circle cx="126" cy="86" r="56" fill="none" stroke="var(--accent)" stroke-width="1.6" stroke-dasharray="2 3"/>
      <g transform="rotate(-8 126 86)">
        <text x="126" y="66" text-anchor="middle" font-family="Montserrat, Arial, sans-serif" font-weight="800" font-size="13" fill="var(--text-dark)">$170 VALUE</text>
        <text x="126" y="81" text-anchor="middle" font-family="Montserrat, Arial, sans-serif" font-weight="600" font-size="10" fill="var(--text-dark)">DETAILS INSIDE</text>
        <rect x="6" y="92" width="240" height="36" fill="var(--accent)" stroke="#ffffff" stroke-width="2"/>
        <text x="126" y="116" text-anchor="middle" font-family="Montserrat, Arial, sans-serif" font-weight="800" font-size="15" fill="var(--text-dark)">FREE ONLINE WORKSHOP</text>
      </g>
    </svg>

    <h1 class="title-stack">
      <span class="title-line title-line--lead">What Makes My Child’s</span>
      <span class="title-line title-line--accent">Playing Talent</span>
      <span class="title-line title-line--close">Grow?</span>
    </h1>

    <p class="subtitle">A Mother’s Plain Talk Manual for Coaching<br>confident, focused and resilient athletes</p>

    <div class="footer-band">
      <div class="brand">
        <span class="brand-dot"></span>
        <span class="brand-name">Mindfield Coaching</span>
      </div>
      <div class="author">RAFE MONTOYA</div>
    </div>
  </div>
</div>
</body>
</html>
```